Design Announcement and Registration Flyer for Tennis Tournament

Hi we need a tennis flyer with registration page designed.
We need it put into pdf form so that it can be email or added to a website and easily downloaded
Simple, Clear, Fresh design

*** WE ONLY HAVE ONE DAY... WE WILL NOT WAIT FOR TOURNAMENT TO FINSIH ***
*** WE WILL CHOOSE A GOOD DESIGN AS SOON AS WE SEE ONE WE LIKE
*** WE ONLY HAVE ONE DAY

```html
<!DOCTYPE html>
<html lang="en">
<head>
<meta charset="utf-8">
<title>4th Annual Austin Lakeside Tennis Doubles Championship</title>
<link rel="stylesheet" href="https://fonts.googleapis.com/css2?family=Oswald:wght@500;600&family=Black+Ops+One&family=PT+Serif:wght@700&family=Open+Sans:ital,wght@0,400;0,600;0,700;1,600&family=Roboto+Condensed:wght@700&display=swap">
<style>
  :root {
    --crimson: #b71c44;
    --table-red: #c0202a;
    --teal: #1a8f8a;
    --teal-light: #23aaa3;
    --heading-teal: #1d8b8b;
    --ink: #111111;
    --paper-center: #f6f6f6;
    --paper-edge: #c9c9c9;
    --rule: #a9a9a9;
    --ball: #d7e634;
    --ball-edge: #8fae16;
    --white: #ffffff;
  }
  html, body { margin: 0; padding: 0; overflow: hidden; }
  body { width: 848px; height: 1200px; }
  .flyer {
    position: relative;
    width: 848px;
    height: 1200px;
    overflow: hidden;
    background: radial-gradient(ellipse at 50% 40%, var(--paper-center) 0%, #e4e4e4 55%, var(--paper-edge) 100%);
    font-family: "Open Sans", Arial, sans-serif;
    color: var(--ink);
  }
  .abs { position: absolute; }
  .banner { left: 0; top: 0; }
  .banner-title {
    font-family: "Oswald", "Arial Narrow", sans-serif;
    font-weight: 600;
    fill: var(--white);
  }
  .tagline {
    font-family: "Oswald", "Arial Narrow", sans-serif;
    font-weight: 500;
    fill: var(--ink);
  }
  .date-pill {
    left: 266px; top: 294px; width: 358px; height: 75px;
    border-radius: 38px;
    background: linear-gradient(180deg, var(--teal-light) 0%, var(--teal) 60%, #137570 100%);
    box-shadow: 0 5px 8px rgba(0,0,0,0.35);
    display: flex; align-items: center; justify-content: center;
    font-family: "PT Serif", Georgia, serif;
    font-weight: 700; font-size: 31px; color: var(--white);
  }
  .location {
    left: 0; width: 848px; text-align: center;
    font-style: italic; font-weight: 600; font-size: 22px;
  }
  .location-label { top: 412px; }
  .location-label svg { vertical-align: -6px; margin-right: 6px; }
  .location-address { top: 442px; font-size: 23px; }
  .section-heading {
    left: 45px;
    font-family: "Black Ops One", Impact, sans-serif;
    font-size: 20px; letter-spacing: 2px;
    color: var(--heading-teal);
    margin: 0; font-weight: 400;
  }
  .fees {
    left: 57px; top: 529px; width: 731px;
    border-collapse: collapse;
    font-size: 15px; background: rgba(255,255,255,0.15);
  }
  .fees th {
    background: var(--table-red); color: var(--white);
    font-weight: 700; font-size: 17px; height: 30px; padding: 0;
    border: 1px solid #7a1a1a;
  }
  .fees td {
    border: 1px solid #333; text-align: center; vertical-align: top;
    padding: 3px 4px 0; line-height: 24px;
  }
  .fees sup { font-size: 9px; line-height: 0; }
  .fees .col-type { width: 154px; }
  .fees .col-fee { width: 266px; }
  .note {
    left: 0; width: 848px; text-align: center; font-weight: 700; font-size: 13px; margin: 0;
  }
  .note-online { color: var(--heading-teal); }
  .incentive {
    left: 134px; top: 766px; width: 578px; height: 52px;
    border-radius: 26px; background: var(--crimson);
    box-shadow: 0 3px 5px rgba(0,0,0,0.3);
    color: var(--white); font-size: 17.5px; line-height: 23px; text-align: center;
    display: flex; align-items: center; justify-content: center;
  }
  .rule { left: 0; width: 848px; height: 3px; background: var(--rule); }
  .schedule {
    left: 0; width: 848px; text-align: center; font-weight: 700; font-size: 14.5px; margin: 0; line-height: 21px;
  }
  .refunds { color: var(--crimson); }
  .officials {
    left: 241px; top: 1038px; font-weight: 700; font-size: 15px; line-height: 21px;
    display: grid; grid-template-columns: 290px auto; margin: 0;
  }
  .officials dt, .officials dd { margin: 0; }
  .footer {
    left: 0; top: 1123px; width: 848px; height: 77px; background: var(--teal);
    font-family: "Roboto Condensed", "Arial Narrow", sans-serif;
    font-weight: 700; font-size: 20px; color: var(--white);
  }
  .contact { position: absolute; top: 8px; text-align: center; }
  .contact svg { display: block; margin: 0 auto 6px; }
  .contact-web { left: 15px; width: 230px; }
  .contact-mail { left: 290px; width: 320px; }
  .contact-phone { left: 680px; width: 150px; }
</style>
</head>
<body>
<main class="flyer">

  <svg class="abs banner" width="848" height="270" viewBox="0 0 848 270">
    <defs>
      <radialGradient id="ball-shade" cx="40%" cy="35%" r="65%">
        <stop offset="0" stop-color="#eef56a"/>
        <stop offset="0.7" stop-color="var(--ball)"/>
        <stop offset="1" stop-color="var(--ball-edge)"/>
      </radialGradient>
      <path id="title-line-1" d="M 150 150 Q 434 112 718 150"/>
      <path id="title-line-2" d="M 240 192 Q 434 180 628 192"/>
      <path id="tagline-line" d="M 230 262 Q 434 238 640 262"/>
    </defs>
    <path d="M 100 112 Q 434 10 768 112 Q 790 118 790 150 L 790 205 Q 790 232 768 230 Q 434 160 100 230 Q 78 232 78 205 L 78 150 Q 78 118 100 112 Z" fill="var(--crimson)"/>
    <g role="img" aria-label="Tennis ball">
      <circle cx="130" cy="171" r="28" fill="url(#ball-shade)" stroke="#5f7a10" stroke-width="1"/>
    </g>
    <g role="img" aria-label="Tennis ball">
      <circle cx="746" cy="171" r="28" fill="url(#ball-shade)" stroke="#5f7a10" stroke-width="1"/>
    </g>
    <text class="banner-title" font-size="31" text-anchor="middle">
      <textPath href="#title-line-1" startOffset="50%">4TH  ANNUAL AUSTIN "LAKESIDE" TENNIS</textPath>
    </text>
    <text class="banner-title" font-size="31" text-anchor="middle">
      <textPath href="#title-line-2" startOffset="50%">DOUBLES CHAMPIONSHIP</textPath>
    </text>
    <text class="tagline" font-size="14" text-anchor="middle">
      <textPath href="#tagline-line" startOffset="50%">“THE LOVE OF THE GAME PASSED DOWN THROUGH GENERATIONS”</textPath>
    </text>
  </svg>

  <div class="abs date-pill">APRIL 20-22, 2018</div>

  <p class="abs location location-label" style="margin:0">
    <svg width="22" height="30" viewBox="0 0 22 30" aria-hidden="true">
      <path d="M11 0 C4.9 0 0 4.9 0 11 C0 19 11 30 11 30 C11 30 22 19 22 11 C22 4.9 17.1 0 11 0 Z" fill="var(--ink)"/>
      <circle cx="11" cy="11" r="4.5" fill="var(--paper-center)"/>
    </svg>Tournament Location:
  </p>
  <p class="abs location location-address" style="margin:0">Brookfield Tennis Center, 4120 Meadowlark Rd., Austin, TX 78799</p>

  <h2 class="abs section-heading" style="top:499px">REGISTERATION DEADLINE(S):</h2>

  <table class="abs fees">
    <thead>
      <tr>
        <th class="col-type">Registerations</th>
        <th class="col-fee">Reg. Fee</th>
        <th>Date of Registeration Closing</th>
      </tr>
    </thead>
    <tbody>
      <tr>
        <td>Early Bird Reg.</td>
        <td>$8 off Total Registeration</td>
        <td>Closed Wednesday, March 14<sup>th</sup> 11pm</td>
      </tr>
      <tr style="height:55px">
        <td>Regular Reg.</td>
        <td>$35 per person for 1<sup>st</sup> event<br>$30 per person for 2<sup>nd</sup> event</td>
        <td>Closed Wednesday. April 11<sup>th</sup> 11pm</td>
      </tr>
      <tr style="height:54px">
        <td>Late Reg.</td>
        <td>$5 Penalty fee added</td>
        <td>Final Closing Saturday, April 14<sup>th</sup><br>11pm</td>
      </tr>
    </tbody>
  </table>

  <p class="abs note" style="top:702px">Mail-in entries must be received WITH PAYMENT no later than Saturday April 14th, 2018</p>
  <p class="abs note note-online" style="top:732px">Online Registerations: http://www.courtentry-demo.com/tourney/home.asp?TID=10472</p>

  <div class="abs incentive">NEW INCENTIVE BONUS: Recruit 4 New Participants and<br>Get Free Credit Entry for one of your Events</div>

  <div class="abs rule" style="top:830px"></div>

  <h2 class="abs section-heading" style="top:856px">TOURNAMENT DATES AND TIMES:</h2>
  <p class="abs schedule" style="top:890px">Tournament begins: 4pm Friday, April 22nd.  (Match times will be online after draw is posted)<br>Draws will be available after 7:00 pm, Monday, April 18th.</p>
  <p class="abs schedule refunds" style="top:952px">Refunds:  No refund after draw is made.</p>

  <div class="abs rule" style="top:993px"></div>

  <h2 class="abs section-heading" style="top:1010px">TOURNAMENT OFFICIALS:</h2>
  <dl class="abs officials">
    <dt>Director:</dt><dd>Dana Whitfield</dd>
    <dt>Assistant Director:</dt><dd>Marcus Ellery</dd>
    <dt>Referee:</dt><dd>Jordan Pike</dd>
    <dt>Assistant Referee:</dt><dd>Luis Carrasco</dd>
  </dl>

  <footer class="abs footer">
    <div class="contact contact-web">
      <svg width="30" height="30" viewBox="0 0 30 30" aria-hidden="true">
        <circle cx="15" cy="15" r="13" fill="none" stroke="var(--white)" stroke-width="2.5"/>
        <ellipse cx="15" cy="15" rx="6" ry="13" fill="none" stroke="var(--white)" stroke-width="2"/>
        <line x1="2" y1="15" x2="28" y2="15" stroke="var(--white)" stroke-width="2"/>
        <line x1="4" y1="8" x2="26" y2="8" stroke="var(--white)" stroke-width="1.6"/>
        <line x1="4" y1="22" x2="26" y2="22" stroke="var(--white)" stroke-width="1.6"/>
      </svg>
      AustinLakesideTennis.com
    </div>
    <div class="contact contact-mail">
      <svg width="38" height="30" viewBox="0 0 38 30" aria-hidden="true">
        <rect x="2" y="5" width="34" height="22" fill="none" stroke="var(--white)" stroke-width="2.5"/>
        <polyline points="2,5 19,19 36,5" fill="none" stroke="var(--white)" stroke-width="2.5"/>
        <line x1="2" y1="27" x2="15" y2="16" stroke="var(--white)" stroke-width="2"/>
        <line x1="36" y1="27" x2="23" y2="16" stroke="var(--white)" stroke-width="2"/>
      </svg>
      Austin.LakesideTennis@example.com
    </div>
    <div class="contact contact-phone">
      <svg width="26" height="30" viewBox="0 0 26 26" aria-hidden="true">
        <path d="M6 2 L10 2 L12 8 L9 10 C10.5 13.5 12.5 15.5 16 17 L18 14 L24 16 L24 20 C24 22 22 24 20 24 C10 23 3 16 2 6 C2 4 4 2 6 2 Z" fill="var(--white)"/>
      </svg>
      512-555-0147
    </div>
  </footer>

</main>
</body>
</html>
```